Velvetorchid Hair & Beauty Business Card

Velvetorchid Hair & Beauty is a boutique salon located in the picturesque Lake Taupo NZ. The salon is very luxurious, opulent gold gilded mirrors, chandelier lit, contemporary french decor, sets the mood to create beautiful hair, makeup and all beauty services. Just had a new logo design and now after a new business card.
Logo
14 Kerewhenua Street
Taupo
Phone (07) 384 6139
www.velvetorchid.co.nz
email hair@velvetorchid.co.nz
Lorinda Feltham
Also need a space to put in Stylist name, date, appointment time. thanks;)
Another idea is we could incorporate the wallpaper in the back ground either on the back or front or use an ornate glided frame (around the edge of the card) like on my website where my brides photos flash.
Decided against the wall paper but at least you can see our colour theme for the salon.
Updates

Please check out my updated brief . Thanks :)

Target Market(s)

25-60 years plus, mainly mid age females , wanting the best possible service , high standard of workmanship and money not a problem.

Industry/Entity Type

Boutique

Requirements
Must have
• Gold and silver

```html
<!DOCTYPE html>
<html lang="en">
<head>
<meta charset="utf-8">
<title>Velvetorchid Hair &amp; Beauty – Business Card</title>
<link href="https://fonts.googleapis.com/css2?family=Lato:wght@400;700;900&display=swap" rel="stylesheet">
<style>
  :root {
    --backdrop: #2b2b2b;
    --card: #fbfbfa;
    --gold: #9a8024;
    --gold-deep: #7d6718;
    --silver: #6e6e6e;
    --ink: #4a4a4a;
    --dots: #9a9a9a;
  }
  * { box-sizing: border-box; margin: 0; padding: 0; }
  html, body {
    width: 1200px; height: 900px; overflow: hidden;
    background: var(--backdrop);
    font-family: 'Lato', sans-serif;
  }
  .card {
    position: absolute; left: 260px; width: 680px; height: 388px;
    background: var(--card);
    box-shadow: 0 10px 30px rgba(0,0,0,.5);
    color: var(--ink);
  }
  .card--back { top: 44px; }
  .card--front { top: 468px; }

  /* back: appointment side */
  .appointment { position: absolute; left: 48px; top: 46px; right: 48px; }
  .appointment__badge {
    display: inline-block; background: var(--gold); color: #fff;
    font-weight: 900; font-size: 17px; letter-spacing: .5px;
    padding: 4px 10px; margin-left: 150px;
  }
  .appointment__row {
    display: flex; align-items: flex-end; gap: 10px;
    font-size: 15px; letter-spacing: .5px; margin-top: 22px; color: var(--silver);
  }
  .appointment__fill { flex: 1; border-bottom: 2px dotted var(--dots); height: 14px; }
  .appointment__days {
    display: flex; justify-content: space-between; margin-top: 22px;
    font-weight: 700; font-size: 15px; color: var(--silver);
  }
  .tick-box { display: inline-flex; align-items: center; gap: 6px; }
  .tick-box::after {
    content: ""; width: 22px; height: 20px;
    border: 2px solid var(--gold); border-radius: 3px;
  }
  .brand {
    font-weight: 400; color: var(--silver); letter-spacing: .5px;
    white-space: nowrap; text-align: center; line-height: 1.05;
  }
  .brand__sub {
    display: block; font-size: 13px; letter-spacing: 3px; margin-top: 4px;
    padding-top: 4px; border-top: 1px solid var(--gold);
  }
  .card--back .brand { position: absolute; left: 360px; bottom: 44px; font-size: 36px; }
  .card--front .brand { position: absolute; top: 62px; left: 0; right: 0; font-size: 46px; }
  .card--front .brand__sub { display: inline-block; padding: 4px 60px 0; }

  /* front: contact side */
  .holder { position: absolute; left: 48px; top: 208px; width: 282px; }
  .holder__name { color: var(--gold); font-weight: 900; font-size: 21px; letter-spacing: .5px; }
  .holder__role { font-weight: 700; font-size: 14px; color: var(--silver); letter-spacing: .5px; }
  .holder__tagline { margin-top: 24px; font-weight: 900; font-size: 16px; line-height: 1.5; color: var(--silver); }
  .divider {
    position: absolute; left: 360px; top: 176px; width: 2px; height: 190px;
    background: linear-gradient(var(--card), var(--gold) 30%, var(--gold) 70%, var(--card));
  }
  .contact { position: absolute; left: 388px; top: 176px; font-size: 16px; color: var(--ink); }
  .contact__address { color: var(--gold-deep); font-weight: 900; line-height: 1.3; }
  .contact__line { display: flex; align-items: center; gap: 10px; margin-top: 14px; }
  .contact__line svg { width: 18px; height: 16px; }
  .contact__web { margin-top: 16px; font-weight: 900; font-size: 17px; }
</style>
</head>
<body>
  <section class="card card--back" aria-label="Appointment side">
    <div class="appointment">
      <span class="appointment__badge">NEXT APPOINTMENT</span>
      <div class="appointment__row">
        <span>DATE:</span><span class="appointment__fill"></span>
        <span>TIME:</span><span class="appointment__fill"></span>
        <span class="tick-box">AM</span><span class="tick-box">PM</span>
      </div>
      <div class="appointment__days">
        <span class="tick-box">Mon</span><span class="tick-box">Tue</span>
        <span class="tick-box">Wed</span><span class="tick-box">Thu</span>
        <span class="tick-box">Fri</span><span class="tick-box">Sat</span>
        <span class="tick-box">Sun</span>
      </div>
      <div class="appointment__row">
        <span>NAME OF STYLIST:</span><span class="appointment__fill"></span>
      </div>
    </div>
    <div class="brand">Velvetorchid<span class="brand__sub">HAIR &amp; BEAUTY</span></div>
  </section>

  <section class="card card--front" aria-label="Contact side">
    <div class="brand">Velvetorchid<br><span class="brand__sub">HAIR &amp; BEAUTY</span></div>
    <div class="holder">
      <p class="holder__name">LORINDA FELTHAM</p>
      <p class="holder__role">DESIGNATION</p>
      <p class="holder__tagline">Premier Wedding, Bridal Hair<br>&amp; Make-up Artists in a calm,<br>private lakeside studio</p>
    </div>
    <div class="divider"></div>
    <div class="contact">
      <p class="contact__address">14 Kerewhenua Street<br>Kahurangi Bay, New Zealand 3384</p>
      <p class="contact__line">
        <svg viewBox="0 0 18 16" aria-hidden="true"><path fill="#4a4a4a" d="M1 5c3-4 13-4 16 0l-2 2-3-1V4H6v2L3 7z M4 8h10l2 7H2z"/></svg>
        (07) 384 6139
      </p>
      <p class="contact__line">
        <svg viewBox="0 0 18 16" aria-hidden="true"><path d="M1 2h16v12H1z M2 3l7 6 7-6" fill="none" stroke="#4a4a4a" stroke-width="1.6"/></svg>
        hair@velvetorchid.co.nz
      </p>
      <p class="contact__web">www.velvetorchid.co.nz</p>
    </div>
  </section>
</body>
</html>
```